A register your interest postcard

It is a slightly bigger postcard that wil be inserted inside a brochure. On one side it is to have the logo with the statement "at Corvanne, Byron Bay" underneath. At the bottom it is to say "Register your interest to become an owner at The Keyholders Circle. On the flipside it has the logo in a smaller version with again in smaller writing "Become an owner at The Keyholders Circle". The main point of this side it to say " SMS your name to 0491 562 037 OR Name: Email: Phone:".
I would like a wood-look style postcard. It is for a luxury beach property that uses a lot of distressed wood in the building of the houses.
Industry/Entity Type
Building
Contact Information for Business Card
I would like a wood-look style postcard for a beach property.
Look and feel
Each slider illustrates characteristics of the customer's brand and the style your logo design should communicate.

```html
<!DOCTYPE html>
<html lang="en">
<head>
<meta charset="utf-8">
<title>The Keyholders Circle – Register Your Interest Postcard</title>
<link rel="stylesheet" href="https://fonts.googleapis.com/css2?family=Montserrat:wght@400;600;700;800&display=swap">
<style>
  :root {
    --mint: #73fab1;
    --ink: #0d0d0d;
    --white: #ffffff;
    --wood-dark: #3a3a3a;
    --wood-mid: #7a7a7a;
    --wood-light: #a9a9a9;
    --gap: #ffffff;
  }
  * { margin: 0; padding: 0; box-sizing: border-box; }
  html, body {
    width: 892px;
    height: 1200px;
    overflow: hidden;
    background: var(--gap);
    font-family: "Montserrat", Arial, sans-serif;
  }
  .postcard {
    position: relative;
    width: 892px;
    height: 1200px;
    overflow: hidden;
  }

  /* Front side */
  .front {
    position: absolute;
    left: 0; top: 0;
    width: 892px;
    height: 592px;
  }
  .front__photo {
    position: absolute;
    inset: 0;
    background: radial-gradient(circle at 48% 52%, var(--wood-light) 0%, var(--wood-mid) 35%, var(--wood-dark) 100%);
  }
  .front__brand {
    position: absolute;
    left: 0; right: 0;
    top: 240px;
    text-align: center;
    color: var(--white);
    font-weight: 700;
    font-size: 50px;
    letter-spacing: 1px;
  }
  .front__place {
    position: absolute;
    left: 261px;
    top: 405px;
    color: var(--white);
  }
  .front__place-at {
    display: block;
    font-weight: 400;
    font-size: 25px;
    letter-spacing: 6px;
  }
  .front__place-town {
    display: block;
    font-weight: 700;
    font-size: 38px;
    letter-spacing: 7px;
    line-height: 1.1;
  }

  /* Shared strapline bar */
  .strapline {
    position: absolute;
    left: 13px;
    width: 866px;
    height: 30px;
    display: flex;
    align-items: center;
    justify-content: center;
    font-weight: 700;
    font-size: 16px;
    letter-spacing: 2.6px;
    white-space: nowrap;
  }
  .strapline--front { top: 551px; background: var(--mint); color: var(--ink); }
  .strapline--back  { top: 1156px; background: var(--ink); color: var(--white); }

  /* Back side */
  .back {
    position: absolute;
    left: 0; top: 602px;
    width: 892px;
    height: 598px;
    background: var(--mint);
  }
  .back__brand {
    position: absolute;
    left: 18px;
    top: 22px;
    color: var(--ink);
    font-weight: 700;
    font-size: 20px;
    line-height: 1.05;
    letter-spacing: 0.5px;
    text-transform: uppercase;
  }
  .back__sms {
    position: absolute;
    left: 0; right: 0;
    top: 58px;
    text-align: center;
    color: var(--ink);
    font-size: 26px;
    font-weight: 400;
    letter-spacing: 4px;
  }
  .back__number {
    position: absolute;
    left: 0; right: 0;
    top: 98px;
    text-align: center;
    color: var(--ink);
    font-size: 39px;
    font-weight: 700;
    letter-spacing: 5px;
  }
  .back__dots {
    position: absolute;
    left: 0; right: 0;
    top: 160px;
    text-align: center;
    color: var(--white);
    font-size: 22px;
    font-weight: 700;
    letter-spacing: 5px;
  }
  .back__or {
    position: absolute;
    left: 0; right: 0;
    top: 212px;
    text-align: center;
    color: var(--white);
    font-size: 34px;
    font-weight: 700;
    letter-spacing: 5px;
  }
  .form-field {
    position: absolute;
    left: 228px;
    color: var(--ink);
    font-size: 23px;
    font-weight: 700;
    letter-spacing: 5px;
    white-space: nowrap;
  }
  .form-field--name  { top: 302px; }
  .form-field--email { top: 385px; }
  .form-field--phone { top: 469px; }
</style>
</head>
<body>
<main class="postcard">
  <section class="front">
    <div class="front__photo" role="img" aria-label="Close-up photograph of a weathered cross-section of a tree trunk with cracked growth rings in grey tones"></div>
    <div class="front__brand">The Keyholders Circle</div>
    <div class="front__place">
      <span class="front__place-at">at Corvanne,</span>
      <span class="front__place-town">Byron Bay</span>
    </div>
    <div class="strapline strapline--front">Register your interest to become an owner at The Keyholders Circle</div>
  </section>

  <section class="back">
    <div class="back__brand">The<br>Keyholders<br>Circle</div>
    <p class="back__sms">SMS your name to</p>
    <p class="back__number">0491 562 037</p>
    <p class="back__dots">.....</p>
    <p class="back__or">OR</p>
    <p class="form-field form-field--name">Name.................</p>
    <p class="form-field form-field--email">Email...............</p>
    <p class="form-field form-field--phone">Phone...............</p>
  </section>
  <div class="strapline strapline--back">Register your interest to become an owner at The Keyholders Circle</div>
</main>
</body>
</html>
```